Website design for Interior Designer

We want a modern website design for an Interior designer. The website should include completed and undergoing projects, CV, services, news, contact and media gallery pages.

Target Market(s)

People or companies who want to design their properties.

Industry/Entity Type

Interior

Number of Pages Required

5+ page

Requirements
Must have
• Related to interior design.
• Portrait of the designer.
• Her CV.
• Current and completed projects.
• Colours as the attached document.
• Pages mentioned in the description
Nice to have
• Like these websites – but don't copy them😊
• www.plovanstudio.co.za
• www.brightwellfixes.co.za
• www.tkstudioltd.com
• others-
• www.haraldbeuk.de/en
• www.emfairley.co.uk/
• Hope that gives you a starting point.

```html
<!DOCTYPE html>
<html lang="en">
<head>
<meta charset="utf-8">
<title>Varsen Interiors — Gallery</title>
<link href="https://fonts.googleapis.com/css2?family=Cabin:wght@400;500;600&display=swap" rel="stylesheet">
<style>
:root{
  --nav-bg:rgba(38,38,40,.78);
  --panel-bg:rgba(22,22,24,.82);
  --white:#ffffff;
  --muted:#9a9a9a;
  --accent:#2fe3b6;
  --line:#3fe0c4;
  --control:#6e5a4c;
  --circle-a:#3cc3d2;
  --circle-b:#4c6cf0;
  --logo-a:#f2ef1c;
}
*{margin:0;padding:0;box-sizing:border-box}
html,body{width:1200px;height:675px;overflow:hidden;background:#d9dadc}
body{font-family:"Cabin",sans-serif;color:var(--white)}
.page{position:relative;width:1200px;height:675px;overflow:hidden}
.room-backdrop{position:absolute;inset:0;
  background:
   linear-gradient(90deg,rgba(40,80,190,.0) 0%,rgba(40,80,190,.0) 100%),
   radial-gradient(ellipse 260px 160px at 90px 520px,rgba(30,80,200,.75),transparent 70%),
   linear-gradient(180deg,#c9cbce 0%,#e6e7e9 30%,#d2d3d4 60%,#8b7a6a 85%,#3a3a3c 100%);}
.site-header{position:absolute;left:0;top:0;width:1200px;height:75px;background:var(--nav-bg)}
.brand{position:absolute;left:257px;top:22px;display:flex;align-items:center;gap:8px}
.brand-mark{width:22px;height:22px;background:var(--logo-a)}
.brand-name{font-size:20px;font-weight:600;color:var(--white)}
.main-nav{position:absolute;top:0;left:0;height:75px}
.main-nav a{position:absolute;top:37px;transform:translate(-50%,-50%);text-decoration:none;color:var(--white);font-size:16px;white-space:nowrap;text-shadow:0 1px 3px rgba(0,0,0,.6)}
.main-nav a.is-dim{color:var(--muted)}
.main-nav a.is-active{color:var(--accent)}
.main-nav a.is-boxed{background:rgba(70,70,72,.8);border-radius:6px;width:83px;height:50px;line-height:50px;text-align:center}
.gallery-panel{position:absolute;left:199px;top:94px;width:817px;height:518px;background:var(--panel-bg);border-radius:9px}
.thumb{position:absolute;width:150px;height:149px;box-shadow:0 0 6px 2px rgba(255,255,255,.75);border:1px solid rgba(255,255,255,.8)}
.feature{position:absolute;left:402px;top:177px;width:411px;height:286px;box-shadow:0 0 7px 2px rgba(255,255,255,.8);border:1px solid rgba(255,255,255,.8);
  background:radial-gradient(ellipse 200px 120px at 50% 35%,#8a8680,#3a3836 55%,#0d0d0d 100%)}
.caption{position:absolute;left:607px;top:483px;transform:translate(-50%,-50%);font-size:18px;font-weight:500}
.controls{position:absolute;left:0;top:0}
.site-footer{position:absolute;left:0;top:620px;width:1200px;height:55px;background:rgba(40,40,42,.85);border-top:1.5px solid var(--line)}
.footer-text{position:absolute;font-size:14.5px;line-height:19px;font-weight:500;text-shadow:0 1px 3px rgba(0,0,0,.7)}
.social{position:absolute;left:916px;top:14px;display:flex;gap:12px;align-items:center}
.social-item{display:flex;align-items:center;gap:5px;font-size:14px;font-weight:500}
.social-dot{width:22px;height:22px;border-radius:50%}
</style>
</head>
<body>
<div class="page">
  <div class="room-backdrop" role="img" aria-label="Bright interior with a blue sofa, framed art and tall windows"></div>

  <header class="site-header">
    <div class="brand"><span class="brand-mark"></span><span class="brand-name">Varsen</span></div>
    <nav class="main-nav">
      <a style="left:394px" href="#">Home</a>
      <a class="is-dim" style="left:499px" href="#">About me</a>
      <a style="left:599px" href="#">News</a>
      <a style="left:691px" href="#">Services</a>
      <a style="left:791px" href="#">Projects</a>
      <a class="is-boxed" style="left:891px" href="#">Gallery</a>
      <a class="is-active" style="left:988px" href="#">Contact</a>
    </nav>
  </header>

  <main>
    <section class="gallery-panel" aria-label="Gallery"></section>
    <div class="thumb" style="left:213px;top:313px;background:linear-gradient(160deg,#e8e6e2,#b89a7a)" role="img" aria-label="White room with wooden floor"></div>
    <div class="thumb" style="left:255px;top:354px;background:linear-gradient(160deg,#e3c9a8,#c0463a 60%,#e8e4de)" role="img" aria-label="Cafe with white tables and red chairs"></div>
    <div class="thumb" style="left:329px;top:386px;background:linear-gradient(170deg,#b08a5a,#4a4036 55%,#c49466)" role="img" aria-label="Arched hall with long wooden counter"></div>
    <div class="thumb" style="left:852px;top:313px;background:linear-gradient(170deg,#9c6a4a,#c99a78 50%,#6a4434)" role="img" aria-label="Warm-lit bedroom interior"></div>
    <div class="thumb" style="left:814px;top:354px;background:linear-gradient(150deg,#8fa2ac,#4a4e52 55%,#6a4a3a)" role="img" aria-label="Lounge with leather chair and angled ceiling"></div>
    <div class="thumb" style="left:738px;top:392px;background:linear-gradient(170deg,#d6dde0,#8a8c8a 55%,#c8cacb)" role="img" aria-label="Modern kitchen with island and bar stool"></div>
    <div class="feature" role="img" aria-label="Ceiling lamp with white globe shades"></div>
    <p class="caption">Sealing img 1</p>

    <svg class="controls" width="1200" height="675" aria-hidden="true">
      <g fill="none" stroke="var(--control)" stroke-width="5" stroke-linecap="round" stroke-linejoin="round">
        <polyline points="494,558 477,575 494,592"/>
        <polyline points="722,558 739,575 722,592"/>
        <circle cx="608" cy="575" r="33" stroke-width="3"/>
      </g>
      <polygon points="597,558 597,592 626,575" fill="var(--control)"/>
    </svg>
  </main>

  <footer class="site-footer">
    <p class="footer-text" style="left:199px;top:9px">mara@varsenstudio.com<br>Senior Interior Designer</p>
    <p class="footer-text" style="left:707px;top:9px">+965 50418273<br>+44 7712603958</p>
    <p class="footer-text" style="left:835px;top:9px">| Kuwait<br>| UK</p>
    <div class="social">
      <span class="social-item"><span class="social-dot" style="background:var(--circle-a)"></span>Chirp</span>
      <span class="social-item"><span class="social-dot" style="background:var(--circle-b)"></span>Facet</span>
    </div>
  </footer>
</div>
</body>
</html>
```